HOME IMPROVEMENT Business Card

I want a very unique business card. nothing typical and boring. Im open to you ideas. Ive seen cards with gold and silver or color foil and spot UV coatings. Im looking for something that looks cool and grabs attention. I like rounded corners but am open to all suggestions. We are a home improvement company and I will have a presentation folder printed and a catalog printed also and want to keep that same theme. I love the colors in our logo but I am open at looking at a 3rd color that would work with my logo. I hope that helps.
Card should include
Address
Phone
Fax
Email
Website
Target Market(s)
Home owners, people looking to remodel their home
Industry/Entity Type
Home Improvement
Contact Information for Business Card
2871 Maple Crest Avenue Unit 400
Linden Hollow, IL 60093
Phone
Direct Line
Email
Website
Font styles to use
Other font styles liked:
- IM OPEN MINDED
Requirements
Must have
- High end quality look nothing boring I like rounded corners but am open minded
Nice to have
- WOW. I want something nice and impressive.
Should not have
- ??? Not sure

```html
<!DOCTYPE html>
<html lang="en">
<head>
<meta charset="utf-8">
<title>Oakhaven Homes – Business Card</title>
<link href="https://fonts.googleapis.com/css2?family=Montserrat:wght@300;400;600&display=swap" rel="stylesheet">
<style>
  :root{
    --navy:#15134a;
    --navy-deep:#0f0d3c;
    --blue:#0a78d4;
    --cyan:#00aeef;
    --white:#ffffff;
    --muted:#c9c9e0;
    --ink:#3c3c4a;
    --pin:#23232c;
    --backdrop:#e3e4e6;
  }
  *{box-sizing:border-box;margin:0;padding:0}
  html,body{width:1200px;height:800px;overflow:hidden}
  body{
    background:var(--backdrop);
    font-family:"Montserrat",sans-serif;
    position:relative;
  }
  .card{
    position:absolute;
    width:520px;height:300px;
    border-radius:26px;
    overflow:hidden;
    box-shadow:0 14px 30px rgba(0,0,0,.16);
  }
  .card--back{left:50px;top:250px;background:linear-gradient(120deg,var(--navy) 0%,#1d1b5c 45%,var(--navy-deep) 100%)}
  .card--front{left:630px;top:250px;background:var(--white)}
  .card__art{position:absolute;inset:0;width:100%;height:100%}

  .brand{
    font-weight:400;color:var(--white);
    letter-spacing:.6px;white-space:nowrap;
  }
  .back__brand{
    position:absolute;left:0;right:0;top:120px;
    display:flex;align-items:center;justify-content:center;gap:10px;
  }
  .back__brand .brand{font-size:26px}
  .brand__dot{width:12px;height:12px;border-radius:50%;background:var(--cyan)}
  .back__rule{
    position:absolute;left:170px;right:170px;top:162px;height:1px;background:rgba(255,255,255,.25);
  }
  .back__web{
    position:absolute;left:0;right:0;top:172px;
    display:flex;justify-content:center;align-items:center;gap:7px;
    color:var(--muted);font-size:12px;font-weight:300;letter-spacing:.4px;
  }

  .front__identity{
    position:absolute;left:170px;width:200px;top:34px;text-align:center;color:var(--white);
  }
  .front__name{font-size:22px;font-weight:300;letter-spacing:.6px}
  .front__role{font-size:10px;font-weight:300;letter-spacing:.5px;opacity:.85;margin-top:2px}
  .front__badge{
    position:absolute;left:213px;top:78px;width:84px;height:84px;border-radius:50%;
    display:flex;align-items:center;justify-content:center;text-align:center;
  }
  .front__badge .brand{font-size:11px;line-height:1.2;white-space:normal}

  .contacts{
    position:absolute;left:24px;right:20px;top:244px;
    display:flex;justify-content:space-between;align-items:center;
  }
  .contact{display:flex;align-items:center;gap:8px;color:var(--ink);font-size:9.5px;line-height:1.35;font-weight:400}
  .contact__icon{width:22px;height:22px;border-radius:50%;display:flex;align-items:center;justify-content:center;flex:none}
  .contact__icon--blue{background:var(--blue)}
  .contact__icon--dark{background:var(--pin)}
</style>
</head>
<body>

<section class="card card--back" aria-label="Business card back">
  <svg class="card__art" viewBox="0 0 520 300" aria-hidden="true">
    <defs>
      <linearGradient id="sheen" x1="0" y1="0" x2="1" y2="0">
        <stop offset="0" stop-color="#fff" stop-opacity="0"/>
        <stop offset=".5" stop-color="#fff" stop-opacity=".08"/>
        <stop offset="1" stop-color="#fff" stop-opacity="0"/>
      </linearGradient>
    </defs>
    <rect x="110" y="0" width="120" height="300" fill="url(#sheen)"/>
  </svg>
  <div class="back__brand"><span class="brand__dot"></span><span class="brand">Oakhaven Homes</span></div>
  <div class="back__rule"></div>
  <div class="back__web">
    <svg width="11" height="11" viewBox="0 0 12 12" aria-hidden="true"><circle cx="6" cy="6" r="5" fill="none" stroke="#c9c9e0" stroke-width="1"/><ellipse cx="6" cy="6" rx="2.2" ry="5" fill="none" stroke="#c9c9e0" stroke-width="1"/><line x1="1" y1="6" x2="11" y2="6" stroke="#c9c9e0" stroke-width="1"/></svg>
    <span>urwebsitename.com</span>
  </div>
</section>

<section class="card card--front" aria-label="Business card front">
  <svg class="card__art" viewBox="0 0 520 300" aria-hidden="true">
    <rect width="520" height="300" fill="var(--navy)"/>
    <path d="M0,200 C120,120 250,74 520,70 L520,300 L0,300 Z" fill="var(--blue)"/>
    <path d="M0,212 C125,130 255,86 520,86 L520,300 L0,300 Z" fill="var(--cyan)"/>
    <path d="M0,226 C130,142 260,100 520,110 L520,300 L0,300 Z" fill="var(--white)"/>
    <circle cx="255" cy="120" r="45" fill="var(--cyan)"/>
    <circle cx="255" cy="120" r="40" fill="var(--navy)"/>
  </svg>
  <div class="front__identity">
    <div class="front__name">Your Name</div>
    <div class="front__role">Your Position</div>
  </div>
  <div class="front__badge"><span class="brand">Oakhaven<br>Homes</span></div>

  <div class="contacts">
    <div class="contact">
      <span class="contact__icon contact__icon--blue">
        <svg width="11" height="11" viewBox="0 0 12 12" aria-hidden="true"><path d="M2.5 1.5 L4.5 1.5 L5.3 3.8 L4 4.8 C4.6 6.2 5.8 7.4 7.2 8 L8.2 6.7 L10.5 7.5 L10.5 9.5 C10.5 10.2 9.9 10.6 9.2 10.5 C5.2 10 2 6.8 1.5 2.8 C1.4 2.1 1.8 1.5 2.5 1.5 Z" fill="#fff"/></svg>
      </span>
      <span>+000 12345 6789<br>+000 12345 6789</span>
    </div>
    <div class="contact">
      <span class="contact__icon contact__icon--blue">
        <svg width="12" height="12" viewBox="0 0 12 12" aria-hidden="true"><circle cx="6" cy="6" r="5" fill="none" stroke="#fff" stroke-width="1"/><ellipse cx="6" cy="6" rx="2.2" ry="5" fill="none" stroke="#fff" stroke-width="1"/><line x1="1" y1="6" x2="11" y2="6" stroke="#fff" stroke-width="1"/></svg>
      </span>
      <span>urwebsitename.com<br>urname@email.com</span>
    </div>
    <div class="contact">
      <span class="contact__icon contact__icon--dark">
        <svg width="10" height="12" viewBox="0 0 10 12" aria-hidden="true"><path d="M5 0.5 C2.5 0.5 1 2.3 1 4.3 C1 7 5 11.5 5 11.5 C5 11.5 9 7 9 4.3 C9 2.3 7.5 0.5 5 0.5 Z" fill="#fff"/><circle cx="5" cy="4.3" r="1.5" fill="#23232c"/></svg>
      </span>
      <span>2871 Maple Crest Avenue Unit 400<br>Linden Hollow, IL 60093</span>
    </div>
  </div>
</section>

</body>
</html>
```